Consulting, Investors, Joint Venture Website

Founded in April 2018, Marendo Consultants Limited (MCL) is an advisory consulting firm specializing in engaging investors in business ventures in Tanzania.
With extensive experience in construction, energy, oil and gas and the legal professions, our team assembles our expertise that allows foreign investors to set foot and flourish in the Tanzanian market.
MCL is locally owned, founded and registered. Our shareholders are cultured Tanzanian citizens with extensive corporate experience in South Africa, Tanzania, United Kingdom and the United States.

Our mission is to provide responsive and unrivalled professional advice from learned and experienced professionals versed in the local market, with an understanding of the cultural and logistical challenges faced by foreign investors.

Our vision is to provide a complete investor’s package that initiates with company registration, compliance and documentation services and ultimately operational facilitation services.

Target Market(s)

Foreign Investors, International companies

Industry/Entity Type

Business Consultant

Number of Pages Required

5+ page

Requirements
Must have
• It will be 5 pages - Home, About Us, Services, Portfolio, Contact Us
Nice to have
• if it can look like https://www.plorvex.example/
• or https://www.dunetri.example or http://www.quillbrook.example/

```html
<!DOCTYPE html>
<html lang="en">
<head>
<meta charset="utf-8">
<title>Marendo Consultants</title>
<link rel="stylesheet" href="https://fonts.googleapis.com/css2?family=Jost:wght@400;500;600&family=Michroma&display=swap">
<style>
:root{
  --blue:#1f5ba8;
  --blue-dark:#174a8c;
  --ink:#2b2b2b;
  --muted:#6f6f6f;
  --line:#e2e2e2;
  --panel:#f0f0f0;
  --black:#0b0b0b;
  --footer:#141a22;
  --white:#ffffff;
  --star:#f2b01e;
}
*{box-sizing:border-box;margin:0;padding:0}
html,body{width:1200px;height:3025px;overflow:hidden;background:var(--white)}
body{font-family:"Jost",sans-serif;color:var(--ink);position:relative}
.wide{font-family:"Michroma",sans-serif;text-transform:uppercase}
a{color:inherit;text-decoration:none}

/* top bar */
.topbar{position:absolute;left:0;top:0;width:1200px;height:34px;background:var(--black);color:#ddd;font-size:12px;display:flex;align-items:center;padding:0 141px}
.topbar .contact{display:flex;gap:28px;align-items:center}
.topbar .contact span{display:flex;align-items:center;gap:7px}
.topbar .social{margin-left:auto;display:flex;gap:12px}
.topbar .social i{width:10px;height:10px;background:#ddd;display:block}

/* hero */
.hero{position:absolute;left:0;top:34px;width:1200px;height:541px;background:linear-gradient(100deg,#e9eef3 0%,#d9e1e8 45%,#8f9aa6 75%,#6b7580 100%)}
.header{position:absolute;left:0;top:0;width:1200px;height:78px;background:rgba(20,24,30,.82);display:flex;align-items:center;padding:0 141px}
.brand{display:flex;align-items:center;gap:10px;color:var(--white)}
.brand .mark{width:46px;height:46px;background:var(--blue)}
.brand .name{font-family:"Jost",sans-serif;font-weight:600;font-size:30px;letter-spacing:3px;color:#4a86d4}
.nav{margin-left:auto;display:flex;gap:34px;font-size:10px;color:var(--white)}
.hero h1{position:absolute;left:141px;top:222px;width:460px;font-size:24.5px;line-height:35px;font-weight:600;color:#1c1c1c}
.dots{display:flex;gap:6px}
.dots i{width:10px;height:10px;border-radius:50%;background:#9aa3ad;display:block}
.dots i.on{background:var(--blue)}
.hero .dots{position:absolute;left:141px;top:379px}

/* section heading */
.sec-title{display:flex;align-items:center;justify-content:center;gap:12px;font-size:19px;color:#8a8a8a}
.sec-title .mark{width:48px;height:38px;background:var(--blue)}
.sec-title .bar{width:2px;height:34px;background:#8a8a8a}
.sec-title b{color:var(--blue);font-weight:400}
.btn{display:inline-block;background:var(--blue);color:var(--white);font-size:13px;text-align:center;line-height:31px;height:31px}

/* services */
.services{position:absolute;left:0;top:575px;width:1200px;height:555px}
.services .sec-title{position:absolute;left:0;top:70px;width:1200px}
.cards{position:absolute;left:141px;top:139px;display:flex;gap:10px}
.card{width:222px;height:284px;background:var(--white);box-shadow:0 2px 8px rgba(0,0,0,.12);text-align:center}
.card .photo{height:143px}
.card h3{font-size:10.5px;font-weight:400;margin:20px 0 8px;color:#222}
.card h3.active{color:var(--blue)}
.card p{font-size:10.5px;line-height:15px;color:var(--muted);padding:0 18px}
.card .more{display:block;font-size:10.5px;margin-top:14px;color:#444}
.card .more.active{color:var(--blue)}
.services .btn{position:absolute;left:544px;top:453px;width:111px}

/* about */
.about{position:absolute;left:0;top:1130px;width:1200px;height:387px;background:var(--panel)}
.about .photo{position:absolute;left:0;top:0;width:579px;height:387px;background:linear-gradient(135deg,#aac4d8 0%,#6b7f93 50%,#3b4654 100%)}
.about .body{position:absolute;left:608px;top:68px;width:452px}
.about .sec-title{justify-content:flex-start;font-size:15px}
.about .sec-title .mark{width:44px;height:36px}
.about .sec-title small{font-size:9px;color:#8a8a8a;margin-left:-4px}
.about p{font-size:10.5px;line-height:17px;color:var(--muted);margin-top:12px}
.about p strong{color:#333;font-weight:500}
.about p a{color:var(--blue);text-decoration:underline}
.mv{display:flex;gap:30px;margin-top:16px}
.mv div{width:210px}
.mv h4{display:flex;align-items:center;gap:8px;font-size:12px;color:#8a8a8a;font-weight:400}
.mv h4 svg{flex:none}
.mv p{margin-top:10px}
.mv p span{color:var(--blue)}

/* portfolio */
.portfolio{position:absolute;left:0;top:1517px;width:1200px;height:494px}
.portfolio .sec-title{position:absolute;left:0;top:70px;width:1200px}
.works{position:absolute;left:141px;top:137px;display:flex;gap:16px}
.work{width:295px}
.work .photo{height:151px}
.work h3{font-size:13.5px;font-weight:500;margin-top:22px;color:#222}
.work p{font-size:11px;line-height:16px;color:var(--muted);margin-top:6px}
.arrow{position:absolute;top:196px;width:32px;height:32px;display:flex;align-items:center;justify-content:center}
.arrow.prev{left:75px;border:1px solid #bbb;background:var(--white)}
.arrow.next{left:1091px;background:#8f8f8f}
.portfolio .btn{position:absolute;left:544px;top:389px;width:111px}

/* cta */
.cta{position:absolute;left:0;top:2011px;width:1200px;height:258px;background:linear-gradient(100deg,#2a63ae 0%,#3a73bd 50%,#2c62aa 100%);text-align:center;color:var(--white)}
.cta h2{font-weight:400;font-size:24px;line-height:35px;margin-top:62px}
.cta .btn{background:#b3b3b3;width:150px;margin-top:16px;font-size:14px;height:36px;line-height:36px}

/* testimonials */
.testimonials{position:absolute;left:0;top:2269px;width:1200px;height:418px}
.testimonials .sec-title{position:absolute;left:0;top:70px;width:1200px}
.quotes{position:absolute;left:141px;top:139px;display:flex;gap:16px}
.quote{width:295px;height:176px;border:1px solid var(--line);padding:18px 20px}
.quote .who{display:flex;align-items:center;gap:16px}
.quote .avatar{width:54px;height:54px;border-radius:50%;background:linear-gradient(#d9c6b6,#a38a76)}
.quote h4{font-size:10.5px;font-weight:400;color:#222}
.quote .role{font-size:10.5px;color:var(--muted);margin-top:2px}
.stars{display:flex;gap:2px;margin-top:12px}
.quote p{font-size:10.5px;line-height:15px;color:var(--muted);margin-top:10px}
.testimonials .dots{position:absolute;left:580px;top:343px}
.testimonials .dots i{background:#aaa}
.testimonials .dots i.on{background:var(--blue)}

/* footer */
.footer{position:absolute;left:0;top:2687px;width:1200px;height:338px;background:linear-gradient(#1d2530,#0e131a);color:var(--white)}
.footer h2{position:absolute;left:141px;top:48px;font-size:15px;font-weight:400}
.form{position:absolute;left:141px;top:86px;width:590px;height:124px}
.form .field{position:absolute;background:var(--white);color:#777;font-size:10.5px;padding:4px 8px}
.form .submit{position:absolute;left:300px;top:96px;width:290px;height:26px;background:var(--blue);font-size:12px;text-align:center;line-height:26px}
.foot-brand{position:absolute;left:770px;top:92px;display:flex;align-items:center;gap:12px}
.foot-brand .mark{width:60px;height:56px;background:#c9ced4}
.foot-brand .name{font-weight:600;font-size:34px;letter-spacing:4px;color:#c9ced4}
.foot-social{position:absolute;left:862px;top:162px;display:flex;gap:5px}
.foot-social i{width:22px;height:22px;display:block;background:#3a79c6}
.foot-social i:last-child{background:#c8402f}
.info{position:absolute;left:310px;top:222px;display:flex;gap:70px;font-size:13px;color:#ddd}
.info span{display:flex;align-items:center;gap:10px}
.foot-bottom{position:absolute;left:141px;top:282px;width:918px;height:56px;border-top:1px solid rgba(255,255,255,.18);display:flex;align-items:center}
.foot-bottom nav{display:flex;font-size:9px}
.foot-bottom nav a{padding:0 14px;border-left:1px solid #777}
.foot-bottom nav a:first-child{padding-left:0;border:0}
.foot-bottom small{margin-left:auto;font-size:10px;color:#ccc}
</style>
</head>
<body>

<div class="topbar">
  <div class="contact">
    <span><svg width="12" height="12" viewBox="0 0 24 24"><path fill="#ddd" d="M6.6 10.8a15.1 15.1 0 006.6 6.6l2.2-2.2c.3-.3.7-.4 1-.2 1.1.4 2.3.6 3.6.6.6 0 1 .4 1 1V20c0 .6-.4 1-1 1A17 17 0 013 4c0-.6.4-1 1-1h3.5c.6 0 1 .4 1 1 0 1.3.2 2.5.6 3.6.1.3 0 .7-.2 1z"/></svg>123-456-7890</span>
    <span><svg width="12" height="10" viewBox="0 0 24 18"><path fill="#ddd" d="M0 0h24v18H0z"/><path fill="none" stroke="#0b0b0b" stroke-width="2" d="M1 1l11 9 11-9"/></svg>info@marendoconsultants.example</span>
  </div>
  <div class="social"><i></i><i></i><i></i><i></i></div>
</div>

<section class="hero" role="img" aria-label="Photo of two smiling businessmen meeting over coffee and a laptop in a bright office">
  <header class="header">
    <div class="brand"><span class="mark"></span><span class="name">MARENDO</span></div>
    <nav class="nav wide"><a>Home</a><a>About Us</a><a>Services</a><a>Portfolio</a><a>Contact Us</a></nav>
  </header>
  <h1>We Are A Advisory Consulting Firm Specializing In Engaging Investors In Business Ventures In Tanzania</h1>
  <div class="dots"><i class="on"></i><i></i><i></i></div>
</section>

<section class="services">
  <div class="sec-title wide"><span class="mark"></span><span class="bar"></span><span>Our <b>Services</b></span></div>
  <div class="cards">
    <article class="card">
      <div class="photo" role="img" aria-label="Construction workers in hard hats on a building site" style="background:linear-gradient(160deg,#c9d6e2,#8b7a5c 60%,#d0a53a)"></div>
      <h3 class="wide">Construction</h3>
      <p>Lorem ipsum dolor sit amet constetuer adipiscing elit, sed diam nonummy nibh euismod tincidunt ut laoreet dolore.</p>
      <a class="more">Read More ›</a>
    </article>
    <article class="card">
      <div class="photo" role="img" aria-label="Rows of solar panels under a blue sky" style="background:linear-gradient(170deg,#2f7fd6,#7fb6ec 45%,#1f4f94)"></div>
      <h3 class="wide active">Energy</h3>
      <p>Lorem ipsum dolor sit amet constetuer adipiscing elit, sed diam nonummy nibh euismod tincidunt ut laoreet dolore.</p>
      <a class="more active">Read More ›</a>
    </article>
    <article class="card">
      <div class="photo" role="img" aria-label="Offshore oil rig at sea" style="background:linear-gradient(170deg,#d8c9a4,#b3803f 45%,#2e6c8f)"></div>
      <h3 class="wide">Oil and Gas</h3>
      <p>Lorem ipsum dolor sit amet constetuer adipiscing elit, sed diam nonummy nibh euismod tincidunt ut laoreet dolore.</p>
      <a class="more">Read More ›</a>
    </article>
    <article class="card">
      <div class="photo" role="img" aria-label="Hand signing a legal document" style="background:linear-gradient(160deg,#ece8e4,#cdbfb6 55%,#9a8c84)"></div>
      <h3 class="wide">Legal Works</h3>
      <p>Lorem ipsum dolor sit amet constetuer adipiscing elit, sed diam nonummy nibh euismod tincidunt ut laoreet dolore.</p>
      <a class="more">Read More ›</a>
    </article>
  </div>
  <a class="btn">Get Started</a>
</section>

<section class="about">
  <div class="photo" role="img" aria-label="Team of business people reviewing documents around a glass table"></div>
  <div class="body">
    <div class="sec-title wide"><span class="mark"></span><span class="bar"></span><span>About <b>Marendo</b></span><small>Consultants</small></div>
    <p><strong>We are an new advisory consulting firm specializing in engaging investors in business ventures in Tanzania.</strong><br>Having extensive experience in construction, energy, oil and gas and the legal professions, our team assembles our expertise that allows foreign investors to set foot and flourish in the Tanzanian market...<a>Read More</a></p>
    <div class="mv">
      <div>
        <h4 class="wide"><svg width="24" height="24" viewBox="0 0 24 24"><circle cx="11" cy="13" r="9" fill="none" stroke="#1f5ba8" stroke-width="2"/><circle cx="11" cy="13" r="4" fill="none" stroke="#1f5ba8" stroke-width="2"/><path d="M11 13L21 3" stroke="#1f5ba8" stroke-width="2"/></svg>Our Mission</h4>
        <p>Our mission is to provide responsive and unrivalled professional advice...<span>[+]</span></p>
      </div>
      <div>
        <h4 class="wide"><svg width="20" height="24" viewBox="0 0 20 24"><circle cx="10" cy="9" r="7" fill="#1f5ba8"/><rect x="6" y="16" width="8" height="5" fill="#1f5ba8"/></svg>Our Vision</h4>
        <p>Our vision is to provide a complete investor's package that initiates...<span>[+]</span></p>
      </div>
    </div>
  </div>
</section>

<section class="portfolio">
  <div class="sec-title wide"><span class="mark"></span><span class="bar"></span><span>Our <b>Portfolio</b></span></div>
  <div class="arrow prev"><svg width="14" height="10" viewBox="0 0 14 10"><path d="M13 5H2M5 1L1 5l4 4" fill="none" stroke="#333" stroke-width="1.6"/></svg></div>
  <div class="works">
    <article class="work">
      <div class="photo" role="img" aria-label="Crane and building silhouette against a sunset sky" style="background:linear-gradient(#7d8ea0,#e0a86a 65%,#3a2c22)"></div>
      <h3>Lorem Ipsum Dolor Sit Amet Constetuer</h3>
      <p>Lorem ipsum dolor sit amet constetuer adipiscing elit, diam nonummy nibh euismod tinc laoreet dolore.</p>
    </article>
    <article class="work">
      <div class="photo" role="img" aria-label="Solar panels and wind turbine under a cloudy blue sky" style="background:linear-gradient(#5d9fe0,#dbe8f4 45%,#2b5fa3)"></div>
      <h3>Lorem Ipsum Dolor Sit Amet Constetuer</h3>
      <p>Lorem ipsum dolor sit amet constetuer adipiscing elit, diam nonummy nibh euismod tinc laoreet dolore.</p>
    </article>
    <article class="work">
      <div class="photo" role="img" aria-label="Offshore oil platform on a calm sea" style="background:linear-gradient(#3b7fd0,#8fbbe6 50%,#1c4b80)"></div>
      <h3>Lorem Ipsum Dolor Sit Amet Constetuer</h3>
      <p>Lorem ipsum dolor sit amet constetuer adipiscing elit, diam nonummy nibh euismod tinc laoreet dolore.</p>
    </article>
  </div>
  <div class="arrow next"><svg width="14" height="10" viewBox="0 0 14 10"><path d="M1 5h11M9 1l4 4-4 4" fill="none" stroke="#fff" stroke-width="1.6"/></svg></div>
  <a class="btn">View All</a>
</section>

<section class="cta" role="img" aria-label="Blue tinted photo of a business handshake behind the call to action">
  <h2>Are You Looking For Professional Advice For Your<br>New Business?</h2>
  <a class="btn">Call Us Today</a>
</section>

<section class="testimonials">
  <div class="sec-title wide"><span class="mark"></span><span class="bar"></span><span>Client <b>Testimonials</b></span></div>
  <div class="quotes">
    <article class="quote">
      <div class="who"><span class="avatar" role="img" aria-label="Client portrait"></span><div><h4 class="wide">Nadia Rowe</h4><div class="role">Lorem ipsum</div></div></div>
      <div class="stars"><svg width="62" height="10" viewBox="0 0 62 10"><g fill="none" stroke="#f2b01e"><path id="s1" d="M5 .8l1.2 2.8 3 .2-2.3 2 .7 3L5 7.2 2.4 8.8l.7-3-2.3-2 3-.2z"/><use href="#s1" x="12.5"/><use href="#s1" x="25"/><use href="#s1" x="37.5"/><use href="#s1" x="50"/></g></svg></div>
      <p>Lorem ipsum dolor sit amet constetuer adipiscing elit, sed diam nonummy nibh euismod tincidunt ut laoreet dolore sit amet constetuer.</p>
    </article>
    <article class="quote">
      <div class="who"><span class="avatar" role="img" aria-label="Client portrait"></span><div><h4 class="wide">Elias Moran</h4><div class="role">Lorem ipsum</div></div></div>
      <div class="stars"><svg width="62" height="10" viewBox="0 0 62 10"><g fill="none" stroke="#f2b01e"><use href="#s1"/><use href="#s1" x="12.5"/><use href="#s1" x="25"/><use href="#s1" x="37.5"/><use href="#s1" x="50"/></g></svg></div>
      <p>Lorem ipsum dolor sit amet constetuer adipiscing elit, sed diam nonummy nibh euismod tincidunt ut laoreet dolore sit amet constetuer.</p>
    </article>
    <article class="quote">
      <div class="who"><span class="avatar" role="img" aria-label="Client portrait"></span><div><h4 class="wide">Grace Lindo</h4><div class="role">Lorem ipsum</div></div></div>
      <div class="stars"><svg width="62" height="10" viewBox="0 0 62 10"><g fill="none" stroke="#f2b01e"><use href="#s1"/><use href="#s1" x="12.5"/><use href="#s1" x="25"/><use href="#s1" x="37.5"/><use href="#s1" x="50"/></g></svg></div>
      <p>Lorem ipsum dolor sit amet constetuer adipiscing elit, sed diam nonummy nibh euismod tincidunt ut laoreet dolore sit amet constetuer.</p>
    </article>
  </div>
  <div class="dots"><i class="on"></i><i></i><i></i></div>
</section>

<footer class="footer" role="group" aria-label="Contact area over a dark night city skyline">
  <h2 class="wide">Contact Us</h2>
  <div class="form">
    <div class="field" style="left:0;top:0;width:290px;height:26px">Name</div>
    <div class="field" style="left:0;top:32px;width:290px;height:26px">Email</div>
    <div class="field" style="left:0;top:64px;width:290px;height:26px">Phone</div>
    <div class="field" style="left:300px;top:0;width:290px;height:64px">Message</div>
    <div class="submit">Submit</div>
  </div>
  <div class="foot-brand"><span class="mark"></span><span class="name">MARENDO</span></div>
  <div class="foot-social"><i></i><i></i><i></i><i></i></div>
  <div class="info">
    <span><svg width="14" height="18" viewBox="0 0 14 18"><path d="M7 1a6 6 0 00-6 6c0 4.5 6 10 6 10s6-5.5 6-10a6 6 0 00-6-6z" fill="none" stroke="#ddd" stroke-width="1.4"/><circle cx="7" cy="7" r="2" fill="#ddd"/></svg>123, Lorem ipsum dolor</span>
    <span><svg width="16" height="16" viewBox="0 0 24 24"><path fill="none" stroke="#ddd" stroke-width="1.6" d="M6.6 10.8a15.1 15.1 0 006.6 6.6l2.2-2.2c.3-.3.7-.4 1-.2 1.1.4 2.3.6 3.6.6.6 0 1 .4 1 1V20c0 .6-.4 1-1 1A17 17 0 013 4c0-.6.4-1 1-1h3.5c.6 0 1 .4 1 1 0 1.3.2 2.5.6 3.6.1.3 0 .7-.2 1z"/></svg>123-456-7890</span>
    <span><svg width="18" height="13" viewBox="0 0 24 18"><rect x="1" y="1" width="22" height="16" fill="none" stroke="#ddd" stroke-width="1.6"/><path fill="none" stroke="#ddd" stroke-width="1.6" d="M1 1l11 9 11-9"/></svg>info@marendoconsultants.example</span>
  </div>
  <div class="foot-bottom">
    <nav class="wide"><a>Home</a><a>About Us</a><a>Services</a><a>Portfolio</a><a>Contact Us</a></nav>
    <small>Copyright © 2018 Marendo Consultants . All Rights Reserved.</small>
  </div>
</footer>

</body>
</html>
```